Tender Lantern Letterhead Design Project

We need a letterhead design for a consultancy business based in Australia.

Tender Lantern is a unique business designed to assist with the complex and time consuming nature of selecting contractors, showing them what to do and reviewing quotes when it comes to body corporate and strata maintenance items such as painting, waterproofing, plumbing and electrical.

Target Market(s)

apartment managers

Industry/Entity Type

Business

Requirements
Must have
• must have logo and contact details

Tender Lantern
82 Corvalla Ridge Road
Tarrowin, QLD 4871
Ph 07 5391 2846
Fax 07 5392 8071
Mobile 0438 917204

```html
<!DOCTYPE html>
<html lang="en">
<head>
<meta charset="utf-8">
<title>Tender Lantern Letterhead</title>
<link rel="stylesheet" href="https://fonts.googleapis.com/css2?family=Arimo:wght@400;700&display=swap">
<style>
  :root {
    --paper: #ffffff;
    --brand-grey: #9b9b9b;
    --brand-red: #c01a24;
    --wash-pink: #fbe3da;
    --ink-light: #ffffff;
  }
  * { margin: 0; padding: 0; box-sizing: border-box; }
  html, body {
    width: 847px;
    height: 1200px;
    overflow: hidden;
    background: var(--paper);
    font-family: "Arimo", Arial, sans-serif;
  }
  .letterhead {
    position: relative;
    width: 847px;
    height: 1200px;
    background: var(--paper);
    overflow: hidden;
  }
  .brand {
    position: absolute;
    left: 57px;
    top: 50px;
  }
  .brand__name {
    display: flex;
    align-items: center;
    gap: 10px;
    font-size: 44px;
    font-weight: 700;
    color: var(--brand-grey);
    letter-spacing: -0.5px;
    line-height: 1;
  }
  .brand__dot {
    width: 14px;
    height: 14px;
    border-radius: 50%;
    background: var(--brand-red);
  }
  .backdrop-wash {
    position: absolute;
    left: 0;
    top: 0;
    width: 847px;
    height: 1200px;
  }
  .contact-panel {
    position: absolute;
    left: 0;
    top: 1022px;
    width: 220px;
    height: 126px;
    background: var(--brand-red);
    border-radius: 0 12px 12px 0;
    padding: 16px 12px 0 46px;
    color: var(--ink-light);
    font-size: 11.5px;
    line-height: 15.5px;
  }
  .contact-panel__name { font-weight: 700; }
  .contact-panel__label { display: inline-block; width: 18px; }
</style>
</head>
<body>
  <main class="letterhead">
    <svg class="backdrop-wash" viewBox="0 0 847 1200" aria-hidden="true">
      <circle cx="810" cy="600" r="345" fill="var(--wash-pink)" opacity="0.75"/>
    </svg>

    <header class="brand">
      <div class="brand__name">Tender Lantern <span class="brand__dot"></span></div>
    </header>

    <footer class="contact-panel">
      <div class="contact-panel__name">Tender Lantern</div>
      <div>82 Corvalla Ridge Road</div>
      <div>Tarrowin, QLD 4871</div>
      <div><span class="contact-panel__label">P:</span>07 5391 2846</div>
      <div><span class="contact-panel__label">F:</span>07 5392 8071</div>
      <div><span class="contact-panel__label">M:</span>0438 917204</div>
    </footer>
  </main>
</body>
</html>
```